Business Card Design - Furniture Retail

Open to both Single or double sided design

We are launching a online ecommerce store that sells Scandinavian/Danish style of furniture in Australia.

We aspire to provide stylish but classic and designers' selection of furniture to the Australia public at affordable price. For the style of the furniture we are selling, please see the following links:

https://www.filecrate.example/sh/qk3mzr8wlp/BXTpLnR4vQ7cYdHs?dl=0

The style of the design we are looking for is clean, simple that look Scandinavian/Danish but yet it is timeless classic.

Aspiring Design
http://www.lindmora.com
http://tobyquell.com.au/
http://vekt.furniture/
http://www.olvo.com/
Updates

Please display the card on normal angle for both front and back instead of funny angle. Please keep it display when displaying the design of the business cards so that we can focus on the designs rather than being confused by the unnecessary stuffs like the hands or background

I think there is already enough curve line on the logo itself so anything extra of the curve on the business card would be really unnecessary. Please avoid using any of the extra curve line on the business card, other than the logo itself. Thanks

Regular card and give them a matt celloglaze to create texture on card that makes it looked luxury and expensive.

Please display design on normal angle! Please only use white colour in the background (not the business card but the referring to the submission) rather than anything fancy so that we can focus on the design.

Target Market(s)

High end market consumers who are financially capable and who has good taste and appreciate good design

aged between 28 - 45 white collars professional/businessmen who live in metropolitan areas

Industry/Entity Type

Business

Font styles to use
Serif
Sans Serif

Requirements
Must have
• Regular card and give them a matt celloglaze to create texture on card that makes it looked luxury and expensive.

Please use the logo from the uploaded files

Company Name: Milo Verhagen
Name: Milo Reeb
Phone: +614 27 305 641
Website: www.miloverhagen.com.au
Email: milo@miloverhagen.com.au
Nice to have
• Colour is not limited to black and white
Should not have
• The concept photos of the furniture should NOT be used in the FRONT page of the business card.

```html
<!DOCTYPE html>
<html lang="en">
<head>
<meta charset="utf-8">
<title>Milo Verhagen – Business Card</title>
<link rel="stylesheet" href="https://fonts.googleapis.com/css2?family=Cinzel:wght@400;500&family=Open+Sans:wght@400&display=swap">
<style>
  :root {
    --page-bg: #ffffff;
    --card-light: #ece6e0;
    --card-dark: #141414;
    --ink-dark: #1a1a1a;
    --ink-muted: #4a4a4a;
    --ink-light: #f5f5f5;
  }
  html, body {
    margin: 0;
    padding: 0;
    width: 1200px;
    height: 750px;
    overflow: hidden;
    background: var(--page-bg);
  }
  .canvas {
    position: relative;
    width: 1200px;
    height: 750px;
  }
  .card {
    position: absolute;
    top: 218px;
    width: 492px;
    height: 281px;
    border-radius: 18px;
    box-shadow: 0 3px 10px rgba(0,0,0,0.18);
    overflow: hidden;
  }
  .card-front {
    left: 97px;
    background: var(--card-light);
    color: var(--ink-dark);
  }
  .card-back {
    left: 601px;
    background: var(--card-dark);
    color: var(--ink-light);
  }
  .brand-name {
    position: absolute;
    margin: 0;
    font-family: "Cinzel", serif;
    font-weight: 500;
    white-space: nowrap;
    letter-spacing: 0.5px;
  }
  .card-front .brand-name {
    left: 67px;
    top: 62px;
    font-size: 35px;
  }
  .card-back .brand-name {
    left: 0;
    right: 0;
    top: 133px;
    text-align: center;
    font-size: 27px;
  }
  .person-name {
    position: absolute;
    left: 67px;
    top: 170px;
    margin: 0;
    font-family: "Cinzel", serif;
    font-weight: 500;
    font-size: 20px;
    letter-spacing: 0.5px;
  }
  .contact-list {
    position: absolute;
    left: 246px;
    top: 171px;
    margin: 0;
    padding: 0;
    list-style: none;
    font-family: "Open Sans", sans-serif;
    font-size: 12.5px;
    color: var(--ink-muted);
  }
  .contact-item {
    display: flex;
    align-items: center;
    height: 20px;
  }
  .contact-icon {
    width: 13px;
    height: 13px;
    margin-right: 9px;
    fill: var(--ink-dark);
    stroke: var(--ink-dark);
  }
</style>
</head>
<body>
<main class="canvas">
  <section class="card card-front" aria-label="Card front">
    <h1 class="brand-name">Milo Verhagen</h1>
    <p class="person-name">Milo Reeb</p>
    <ul class="contact-list">
      <li class="contact-item">
        <svg class="contact-icon" viewBox="0 0 14 14" aria-hidden="true">
          <path d="M1 4 Q7 0 13 4 L12 6 L9.5 5 L9.5 4 Q7 3 4.5 4 L4.5 5 L2 6 Z" stroke="none"/>
          <rect x="3" y="7" width="8" height="6" rx="1" stroke="none"/>
        </svg>
        <span>+614 27 305 641</span>
      </li>
      <li class="contact-item">
        <svg class="contact-icon" viewBox="0 0 14 14" aria-hidden="true">
          <rect x="1" y="3" width="12" height="8" stroke="none"/>
          <path d="M1 3 L7 8 L13 3" fill="none" stroke="#ece6e0" stroke-width="1.2"/>
        </svg>
        <span>milo@miloverhagen.com.au</span>
      </li>
      <li class="contact-item">
        <svg class="contact-icon" viewBox="0 0 14 14" aria-hidden="true">
          <g fill="none" stroke-width="1">
            <circle cx="7" cy="7" r="5.5"/>
            <ellipse cx="7" cy="7" rx="2.4" ry="5.5"/>
            <line x1="1.5" y1="7" x2="12.5" y2="7"/>
            <line x1="2.5" y1="4.2" x2="11.5" y2="4.2"/>
            <line x1="2.5" y1="9.8" x2="11.5" y2="9.8"/>
          </g>
        </svg>
        <span>www.miloverhagen.com.au</span>
      </li>
    </ul>
  </section>

  <section class="card card-back" aria-label="Card back">
    <p class="brand-name">Milo Verhagen</p>
  </section>
</main>
</body>
</html>
```